Etikett für Pure Ridge CBD Öl
Zielgruppe
Die Marke Pure Ridge verkauft CBD Hanf Öl.
Aufgabenstellung
Ich habe Ihnen ein Referenzprodukt bereitgestellt von meiner baldigen Marke Sky Drift, damit Sie sich etwas darunter vorstellen können.
-Was auf die Flasche drauf muss:
vorne:
das Logo Pure ridge
Hanf Öl
CBD aus Co2 Extraktion
Nahrungsergänzungsmittel
10 ml
Ich lasse mich mal überraschen, was Sie mir für Designs fertigstellen.
Bevorzugte Farben: weiß, Royal blue, schwarz, Gold, grün
Stellen Sie ein Design, dass zu dem Logo Pure Ridge passt.
Es soll sehr hochwertig aussehen. Auf den Gewinner warten regelmäßig weitere Produktdesigns und andere Designarbeiten von Pure Ridge aus Deutschland und Sky Drift aus Spanien.
hinten klein:
Empfohlene Tagesdosis: 2x 5-10 Tropfen
Die maximale Tagesdosierung von 20 Tropfen darf nicht überschritten werden
Nahrungsergänzungsmittel dienen nicht als Ersatz für eine abwechslungsreiche und ausgewogene Ernährung.
Lagern Sie das Produkt kühl, dunkel und außerhalb der Reichweite von Kindern.
Zutaten: Hanfsamenöl: 2295mg(77%), Hanfextrakt: 2295 mg(23%)
CBD 500mg, entspricht 37mg/ empfohlener Tagesdosis
Mindestens haltbar bis 01.03.2019
Chargernummer DE/417/6081
Anbaugebiet: EU
Vertrieb: TKB UG
Lindauer Weg 14
71388 Lindenfeld

```html
<!DOCTYPE html>
<html lang="de">
<head>
<meta charset="utf-8">
<title>Pure Ridge – Hanf Öl Etikett</title>
<link href="https://fonts.googleapis.com/css2?family=Marcellus&family=Ubuntu:wght@700&family=Oswald:wght@700&family=Arimo:wght@700&family=Open+Sans:wght@600&display=swap" rel="stylesheet">
<style>
  :root {
    --navy: #23336b;
    --gold: #f5b731;
    --white: #ffffff;
    --black: #111111;
    --green: #1e8a3a;
    --leaf: #5f9e5c;
    --backdrop: #dcdcde;
  }
  * { margin: 0; padding: 0; box-sizing: border-box; }
  html, body { width: 960px; height: 1200px; overflow: hidden; background: var(--backdrop); }
  .canvas { position: relative; width: 960px; height: 1200px; overflow: hidden; }

  .label {
    position: absolute; left: 14px; top: 290px;
    width: 1370px; height: 910px;
    background: var(--navy);
    transform: scale(0.68); transform-origin: 0 0;
  }

  .front-panel {
    position: absolute; left: 42px; top: 47px; width: 600px; height: 740px;
    background: var(--white); border: 6px solid var(--gold); border-radius: 20px;
  }
  .brand-mark {
    position: absolute; left: 0; right: 0; top: 90px;
    display: flex; align-items: center; justify-content: center; gap: 18px;
    font-family: "Marcellus", serif; font-size: 54px; color: var(--leaf);
  }
  .brand-mark .dot { width: 44px; height: 44px; border-radius: 50%; background: var(--leaf); }
  .product-name {
    position: absolute; left: 0; right: 0; top: 300px; text-align: center;
    font-family: "Marcellus", serif; font-weight: 400; font-size: 124px; line-height: 1; color: var(--black);
    letter-spacing: 2px;
  }
  .extraction {
    position: absolute; left: 0; right: 0; top: 442px; text-align: center;
    font-family: "Ubuntu", sans-serif; font-weight: 700; font-size: 45px; color: var(--green);
  }
  .gold-rule { position: absolute; left: 116px; width: 320px; height: 0;
    border-top: 3px solid var(--gold); border-bottom: 3px solid var(--gold); padding-top: 2px; }
  .gold-rule.top { top: 506px; }
  .gold-rule.bottom { top: 584px; }
  .category {
    position: absolute; left: 0; right: 20px; top: 522px; text-align: center;
    font-family: "Oswald", sans-serif; font-weight: 700; font-size: 38px; color: var(--navy);
    transform: scaleX(0.9);
  }
  .volume, .strength {
    position: absolute; top: 670px;
    font-family: "Oswald", sans-serif; font-weight: 700; font-size: 32px; color: var(--black);
  }
  .volume { left: 32px; }
  .strength { right: 54px; }

  .seal {
    position: absolute; left: 242px; top: 690px; width: 200px; height: 200px;
    border-radius: 50%; background: var(--white);
    border: 8px solid var(--gold); box-shadow: inset 0 0 0 14px var(--navy);
    display: flex; align-items: center; justify-content: center;
    font-family: "Marcellus", serif; font-size: 28px; color: var(--navy);
  }

  .back-panel {
    position: absolute; left: 802px; top: 167px; width: 415px; height: 513px;
    background: var(--white); border: 6px solid var(--gold); border-radius: 18px;
    font-family: "Arimo", sans-serif; font-weight: 700; color: var(--black);
    text-align: center; font-size: 18px; line-height: 18px;
  }
  .back-panel p { position: absolute; left: 0; right: 0; }
  .dosage { top: 30px; }
  .notice { top: 140px; }
  .storage { top: 222px; }
  .ingredients { top: 286px; font-size: 20px; line-height: 19px; }
  .cbd-content { top: 344px; font-family: "Open Sans", sans-serif; font-weight: 600; font-size: 13px; }
  .distributor { top: 390px; font-size: 20px; line-height: 17px; }
  .batch { top: 470px; font-family: "Open Sans", sans-serif; font-weight: 600; font-size: 13px; }
  .origin, .best-before {
    position: absolute; top: 486px;
    font-family: "Open Sans", sans-serif; font-weight: 600; font-size: 13px;
  }
  .origin { left: 16px; }
  .best-before { right: 8px; }
</style>
</head>
<body>
<div class="canvas">
  <div class="label">
    <section class="front-panel">
      <div class="brand-mark"><span class="dot"></span><span>Pure Ridge</span></div>
      <h1 class="product-name">HANF ÖL</h1>
      <p class="extraction">CBD aus Co2 Extraktion</p>
      <div class="gold-rule top"></div>
      <p class="category">Nahrungsergänzungsmittel</p>
      <div class="gold-rule bottom"></div>
      <span class="volume">10 ml</span>
      <span class="strength">5 %</span>
      <div class="seal">Pure Ridge</div>
    </section>

    <section class="back-panel">
      <p class="dosage">Empfohlene Tagesdosis: 2x<br>5-10 Tropfen<br>Die maximale Tagesdosierung<br>von 20 Tropfen darf nicht<br>überschritten werden</p>
      <p class="notice">Nahrungsergänzungsmittel dienen nicht als<br>Ersatz für eine abwechslungsreiche und<br>ausgewogene Ernährung.</p>
      <p class="storage">Lagern Sie das Produkt kühl, dunkel und<br>außerhalb der Reichweite von Kindern.</p>
      <p class="ingredients">Zutaten: Hanfsamenöl: 2295mg(77%),<br>Hanfextrakt: 2295 mg(23%)</p>
      <p class="cbd-content">CBD 500mg, entspricht 37mg/ empfohlener Tagesdosis</p>
      <p class="distributor">Vertrieb: TKB UG<br>Lindauer Weg 14<br>71388 Lindenfeld</p>
      <p class="batch">Chargernummer DE/417/6081</p>
      <span class="origin">Anbaugebiet: EU</span>
      <span class="best-before">Mindestens haltbar bis 01.03.2019</span>
    </section>
  </div>
</div>
</body>
</html>
```